Book Cover - for a Murder book

PROJECT DEADLINE JAN 6TH END OF DAY (Seattle Time).
Goal of the project is to design a book cover for a book related to the investigation of the murder of the Mexican presidential candidate Ramiro Esteban Quintanar.
Look at presidential assassination books in Librovia for ideas.
Also look at pictures in the web of Ramiro Esteban Quintanar, for example here:
http://www.fotobuscanet.example/images/search?q=ramiro+esteban+quintanar&FORM=HDRSC2
Must deliver in format that can be modified (either PSD or Illustrator), as well as in PNG.
The author of the book is the most important lawyer in Mexico, so the cover should show that this book is serious, interesting, deep, to be trusted.
Image should contain:
Image: 1563 pixels x 2500 pixels (front page)
- and extend the design to cover the side of the book and the back of the book
Back of the book: a placeholder for a small title, a picture of the author, and a few lines of text
Title of the book: Vecino Ausente
Subtitle (smaller font): El asesinato de Ramiro Esteban Quintanar
Author: Dr. Héctor Villalba Ruano
I will also create a version in English, changing the text to:
Title of the Book: Hollow Witness
Subtitle (smaller font): The assasination of Ramiro Esteban Quintanar
Hi, we've received many great designs, so we have more than enough. We will be making the decision tomorrow, January 6th, end of day.
Serious readers of investigative murders.
Lawyer

```html
<!DOCTYPE html>
<html lang="es">
<head>
<meta charset="utf-8">
<title>Vecino Ausente — cubierta</title>
<link rel="stylesheet" href="https://fonts.googleapis.com/css2?family=Roboto+Condensed:wght@400;700&family=Lato:wght@400&display=swap">
<style>
  :root {
    --backdrop: #c8cecb;
    --cover: #0c0c0c;
    --white: #ececec;
    --red: #9c1a1a;
    --green: #1c6a2b;
    --ink: #1d1d1d;
    --band: #ebebeb;
    --text: #e6e6e6;
  }
  * { margin: 0; padding: 0; box-sizing: border-box; }
  html, body { width: 1200px; height: 950px; overflow: hidden; }
  body { background: var(--backdrop); position: relative; font-family: "Lato", sans-serif; }

  .cover {
    position: absolute; left: 87px; top: 83px; width: 1026px; height: 777px;
    background: var(--cover);
  }

  /* Back */
  .back { position: absolute; left: 0; top: 0; width: 480px; height: 100%; }
  .back-title {
    position: absolute; left: 0; width: 480px; top: 64px; text-align: center;
    font-family: "Roboto Condensed", sans-serif; font-weight: 700; font-size: 33px;
    color: var(--white); letter-spacing: 0.2px;
  }
  .accent { color: var(--red); }
  .back-copy {
    position: absolute; left: 29px; top: 136px; width: 429px;
    font-size: 13.6px; line-height: 18.3px; color: var(--text); text-align: justify;
  }
  .author-photo {
    float: left; width: 118px; height: 155px; margin: 2px 9px 4px 0;
    background: var(--band); color: var(--green); font-size: 14px;
    text-align: center; padding-top: 27px;
  }

  /* Spine */
  .spine {
    position: absolute; left: 480px; top: 0; width: 58px; height: 100%;
    border-left: 1px dashed #2a2a2a; border-right: 1px dashed #2a2a2a;
  }
  .spine-text {
    position: absolute; left: 0; width: 58px; writing-mode: vertical-rl;
    font-family: "Roboto Condensed", sans-serif; display: flex; align-items: center;
  }
  .spine-subtitle { top: 14px; height: 290px; justify-content: flex-start; color: var(--white); font-size: 14.5px; padding-left: 0; }
  .spine-subtitle b { font-weight: 700; font-size: 16px; margin-top: 4px; }
  .spine-rule { position: absolute; left: 6px; width: 46px; height: 3px; background: var(--red); }
  .spine-title { top: 322px; height: 265px; font-weight: 700; font-size: 35px; color: var(--white); justify-content: center; }
  .spine-author { top: 600px; height: 170px; color: var(--white); font-size: 14.5px; }

  /* Front */
  .front { position: absolute; left: 538px; top: 0; width: 488px; height: 100%; }
  .front-title {
    position: absolute; left: 58px; top: 57px;
    font-family: "Roboto Condensed", sans-serif; font-weight: 700;
    font-size: 76px; line-height: 1; color: var(--white);
  }
  .title-band {
    position: absolute; left: 0; top: 139px; width: 297px; height: 81px;
    background: var(--band);
  }
  .title-band span {
    position: absolute; left: 58px; top: -4px;
    font-family: "Roboto Condensed", sans-serif; font-weight: 700;
    font-size: 86px; line-height: 1; color: var(--red);
  }
  .portrait {
    position: absolute; left: 4px; top: 262px; width: 484px; height: 336px;
    background: radial-gradient(ellipse at 50% 55%, #6d6d6d 0%, #3a3a3a 45%, #0c0c0c 80%);
  }
  .target { position: absolute; left: 172px; top: 258px; }
  .subtitle-band {
    position: absolute; left: 3px; top: 597px; width: 485px; height: 62px;
    background: var(--band); display: flex; align-items: center; justify-content: center;
    font-family: "Roboto Condensed", sans-serif; color: var(--ink); font-size: 20px; gap: 6px;
  }
  .subtitle-band b { color: var(--green); font-weight: 700; font-size: 23px; }
  .front-author {
    position: absolute; left: 0; width: 488px; top: 724px; text-align: center;
    font-family: "Roboto Condensed", sans-serif; color: var(--white); font-size: 19px;
  }
</style>
</head>
<body>
  <div class="cover">
    <section class="back">
      <h2 class="back-title">VECINO <span class="accent">AUSENTE</span></h2>
      <div class="back-copy">
        <div class="author-photo">autor photo</div>
        Lorem ipsum dolor sit amet, consectetur adipisicing elit, sed do eiusmod tempor in incididunt ut labore et dolore magna aliqua. Ut enim ad minim veniam, quis do nostrud et do exercitation ullamco laboris nisi ut aliquip ex ea commodo consequat. Duis aute irure dolor in reprehenderit in anim ex voluptate velit esse cillum dolore eu fugiat nulla pariatur. Excepteur sint occaecat mag cupidatat non proident, sunt in culpa qui et officia
        Lorem ipsum dolor sit amet, consectetur adipisicing elit, sed do eiusmod tempor in incididunt ut labore et dolore magna aliqua. Ut enim ad minim veniam, quis do nostrud et exercitation ullamco laboris nisi ut aliquip ex ea commodo consequat. Duis aute irure dolor in reprehenderit in anim ex etta voluptate velit esse cillum dolore eu fugiat nulla pariatur. Enoxcepteur sint occaecat mag cupidatat non proident, sunt in culpa qui et officia deserunt mollit anim id est laborum. Lorem ipsum dolor sit amet, consectetur adipisicing elit, sed do eiusmod tempor eu incididunt ut labore et dolore magna aliqua. Ut enim ad minim veniam, quis.
      </div>
    </section>

    <section class="spine">
      <div class="spine-text spine-subtitle">El asesinato de&nbsp;<b>Ramiro Esteban Quintanar</b></div>
      <div class="spine-rule" style="top:311px"></div>
      <div class="spine-text spine-title">VECINO&nbsp;<span class="accent">AUSENTE</span></div>
      <div class="spine-rule" style="top:592px"></div>
      <div class="spine-text spine-author">Dr. Héctor Villalba Ruano</div>
    </section>

    <section class="front">
      <h1 class="front-title">VECINO</h1>
      <div class="title-band"><span>AUSENTE</span></div>
      <div class="portrait" role="img" aria-label="Black and white halftone photo of the candidate speaking with arms outstretched"></div>
      <svg class="target" width="176" height="176" viewBox="0 0 176 176" aria-hidden="true">
        <g fill="none" stroke="#9c1a1a" stroke-width="7">
          <circle cx="88" cy="88" r="80"/>
          <circle cx="88" cy="88" r="42"/>
          <line x1="88" y1="4" x2="88" y2="66"/>
          <line x1="88" y1="110" x2="88" y2="172"/>
          <line x1="4" y1="88" x2="66" y2="88"/>
          <line x1="110" y1="88" x2="172" y2="88"/>
        </g>
      </svg>
      <div class="subtitle-band">El asesinato de <b>Ramiro Esteban Quintanar</b></div>
      <p class="front-author">Dr. Héctor Villalba Ruano</p>
    </section>
  </div>
</body>
</html>
```